Timid Kitten Clinic Business Card Design

I need a business card designed for my cat only veterinary clinic. I will upload the logo that I would like included on the card. Please include:
Business Name: The Timid Kitten Clinic
Address: 4827 W. 39th Ln, Scottsdale, AZ 85317
Phone #: 480-555-6314
Website URL: www.timidkittenvet.example
And the Doctors Name: Marla Quint, DVM

```html
<!DOCTYPE html>
<html lang="en">
<head>
<meta charset="utf-8">
<title>The Timid Kitten Clinic – Business Card</title>
<link rel="stylesheet" href="https://fonts.googleapis.com/css2?family=Comfortaa:wght@500&family=Fira+Sans:wght@400&family=Figtree:wght@400;500;700&display=swap">
<style>
  :root {
    --stage: #262626;
    --card: #ffffff;
    --ink: #161616;
    --service-ink: #3b4656;
    --bullet: #8d93d8;
    --mark: #2b1d3a;
    --photo-warm-a: #f6eee6;
    --photo-warm-b: #b98d78;
    --photo-warm-c: #4a3038;
    --photo-cool-a: #f4f2f1;
    --photo-cool-b: #e4dfdc;
  }
  * { margin: 0; padding: 0; box-sizing: border-box; }
  html, body { width: 1200px; height: 1200px; overflow: hidden; background: var(--stage); }
  .stage { position: relative; width: 1200px; height: 1200px; }

  .card {
    position: absolute;
    width: 700px; height: 399px;
    background: var(--card);
    border-radius: 25px;
    overflow: hidden;
  }
  .card--front { left: 219px; top: 185px; }
  .card--back  { left: 227px; top: 616px; }

  .photo { position: absolute; top: 0; bottom: 0; right: 0; }
  .card--front .photo {
    left: 320px;
    background:
      linear-gradient(90deg, var(--card) 0%, rgba(255,255,255,0) 45%),
      radial-gradient(ellipse 50% 70% at 72% 55%, var(--photo-warm-c) 0%, var(--photo-warm-b) 45%, var(--photo-warm-a) 85%);
  }
  .card--back .photo {
    left: 218px;
    background:
      linear-gradient(90deg, var(--card) 0%, rgba(255,255,255,0) 30%),
      radial-gradient(ellipse 55% 65% at 55% 50%, var(--photo-cool-b) 0%, var(--photo-cool-a) 80%);
  }

  .brand { position: absolute; display: flex; align-items: center; }
  .brand__dot { border-radius: 50%; background: var(--mark); flex: none; }
  .brand__name {
    font-family: 'Comfortaa', sans-serif;
    font-weight: 500;
    color: var(--ink);
    letter-spacing: 0.06em;
    line-height: 1.05;
  }
  .card--front .brand { left: 49px; top: 31px; }
  .card--front .brand__dot { width: 132px; height: 132px; margin-right: 8px; }
  .card--front .brand__name { font-size: 30px; }
  .card--back .brand { left: 30px; top: 43px; }
  .card--back .brand__dot { width: 122px; height: 122px; margin-right: 7px; }
  .card--back .brand__name { font-size: 28px; }

  .services {
    position: absolute; left: 0; width: 512px; top: 196px;
    font-family: 'Fira Sans', sans-serif;
    font-size: 16px; color: var(--service-ink);
    text-align: center;
  }
  .services__row { height: 42px; line-height: 28px; white-space: nowrap; }
  .services__sep { color: var(--bullet); margin: 0 9px; }

  .person { position: absolute; left: 55px; top: 200px; font-family: 'Figtree', sans-serif; color: var(--ink); }
  .person__name { font-size: 30px; font-weight: 700; line-height: 1; }
  .person__role { font-size: 22px; font-weight: 400; line-height: 1; margin-top: 2px; }

  .contact {
    position: absolute; left: 55px; top: 292px;
    font-family: 'Figtree', sans-serif; font-weight: 700; font-size: 17px; color: var(--ink);
    list-style: none;
  }
  .contact__item { display: flex; align-items: center; height: 21px; }
  .contact__icon { width: 17px; height: 17px; margin-right: 10px; flex: none; }

  .social {
    position: absolute; left: 487px; top: 327px;
    display: flex; align-items: center;
    font-family: 'Figtree', sans-serif; font-weight: 500; font-size: 19px; color: var(--ink);
  }
  .social__dot { width: 28px; height: 28px; border-radius: 50%; background: var(--ink); margin-left: 9px; }
</style>
</head>
<body>
<main class="stage">

  <section class="card card--front">
    <div class="photo" role="img" aria-label="Photo of a fluffy seal-point cat resting by a sunny window"></div>
    <div class="brand">
      <span class="brand__dot"></span>
      <span class="brand__name">The Timid Kitten<br>Clinic</span>
    </div>
    <div class="services">
      <div class="services__row">Feline Dentistry<span class="services__sep">•</span>Surgery<span class="services__sep">•</span>Diagnostics<span class="services__sep">•</span>Cold Laser Therapy</div>
      <div class="services__row">Cat Boarding Services<span class="services__sep">•</span>Cat Grooming Services</div>
      <div class="services__row">Feline Behavioral Therapy<span class="services__sep">•</span>Telemedicine Services</div>
    </div>
  </section>

  <section class="card card--back">
    <div class="photo" role="img" aria-label="Faded photo of a grey and white cat lying on a soft blanket"></div>
    <div class="brand">
      <span class="brand__dot"></span>
      <span class="brand__name">The Timid Kitten<br>Clinic</span>
    </div>
    <div class="person">
      <div class="person__name">Marla Quint, DVM</div>
      <div class="person__role">Director / Doctor</div>
    </div>
    <ul class="contact">
      <li class="contact__item">
        <svg class="contact__icon" viewBox="0 0 24 24"><path fill="currentColor" d="M6.6 10.8a15.1 15.1 0 0 0 6.6 6.6l2.2-2.2a1 1 0 0 1 1-.25 11.4 11.4 0 0 0 3.6.57 1 1 0 0 1 1 1V20a1 1 0 0 1-1 1A17 17 0 0 1 3 4a1 1 0 0 1 1-1h3.5a1 1 0 0 1 1 1c0 1.25.2 2.45.57 3.57a1 1 0 0 1-.25 1z"/></svg>
        (480) 555-6314
      </li>
      <li class="contact__item">
        <svg class="contact__icon" viewBox="0 0 24 24" fill="none" stroke="currentColor" stroke-width="2"><circle cx="12" cy="12" r="9.5"/><path d="M2.5 12h19M12 2.5c3 3 3 16 0 19M12 2.5c-3 3-3 16 0 19"/></svg>
        www.timidkittenvet.example
      </li>
      <li class="contact__item">
        <svg class="contact__icon" viewBox="0 0 24 24"><path fill="currentColor" d="M12 2a7 7 0 0 0-7 7c0 5.2 7 13 7 13s7-7.8 7-13a7 7 0 0 0-7-7zm0 9.5A2.5 2.5 0 1 1 12 6.5a2.5 2.5 0 0 1 0 5z"/></svg>
        4827 W. 39th Ln, Scottsdale, AZ 85317
      </li>
    </ul>
    <div class="social">
      Find us on:
      <span class="social__dot"></span>
      <span class="social__dot"></span>
    </div>
  </section>

</main>
</body>
</html>
```